Bubble map/flip book

I need someone to create a bubble map with explanations using the attached. This will be used to create a color coded flip book/manual. I need you to clean this up.

Mirandalowsky@plinkmail.com

```html
<!DOCTYPE html>
<html lang="en">
<head>
<meta charset="utf-8">
<title>Claim Was Denied</title>
<link rel="stylesheet" href="https://fonts.googleapis.com/css2?family=Arimo:wght@700&family=Open+Sans:ital@1&display=swap">
<style>
  :root {
    --orange: #F5883A;
    --slate: #4E4D46;
    --header-blue: #0A6A9C;
    --white: #FFFFFF;
    --ink: #3A3A3A;
    --yellow: #FFCB2B;
    --magenta: #C55FA5;
    --green: #A8CE45;
    --red: #EA2D5A;
    --lavender: #A07DB6;
    --blue: #009ADB;
    --coral: #EE5E74;
    --footer-grey: #A7A6A0;
    --tab: #3A3A35;
  }
  * { margin: 0; padding: 0; box-sizing: border-box; }
  html, body { width: 927px; height: 1200px; overflow: hidden; }
  body { font-family: "Arimo", Arial, sans-serif; }

  .page {
    position: relative;
    width: 927px;
    height: 1200px;
    background: linear-gradient(to bottom, var(--orange) 0, var(--orange) 328px, var(--slate) 328px);
    overflow: hidden;
  }

  .connector {
    position: absolute;
    top: 398px;
    width: 4px;
    margin-left: -2px;
    box-shadow: 14px 0 12px rgba(0,0,0,0.18);
  }

  .title-bar {
    position: absolute;
    left: 86px; top: 256px;
    width: 756px; height: 144px;
    background: var(--header-blue);
    border: 3px solid var(--white);
    border-radius: 14px;
    box-shadow: 6px 8px 14px rgba(0,0,0,0.35);
    display: flex; align-items: center; justify-content: center;
    z-index: 2;
  }
  .title-bar h1 {
    color: var(--white);
    font-size: 76px;
    font-weight: 700;
    letter-spacing: 0.5px;
    text-shadow: 2px 3px 5px rgba(0,0,0,0.45);
  }

  .reason {
    position: absolute;
    width: 138px; height: 138px;
    padding: 0 6px;
    border-radius: 5px;
    display: flex; align-items: center; justify-content: center;
    text-align: center;
    font-size: 23px;
    line-height: 1.17;
    font-weight: 700;
    color: var(--white);
    box-shadow: 10px 10px 14px rgba(0,0,0,0.35);
    z-index: 2;
  }
  .reason.dark-text { color: var(--ink); }
  .reason.small-text { font-size: 19.5px; line-height: 1.2; padding: 0 2px; }
  .row-top { top: 547px; }
  .row-bottom { top: 778px; }

  .footer-url {
    position: absolute;
    left: 706px; top: 1142px;
    font-family: "Open Sans", Arial, sans-serif;
    font-style: italic;
    font-size: 16px;
    color: var(--footer-grey);
  }
  .page-number {
    position: absolute;
    left: 894px; top: 1138px;
    width: 33px; height: 32px;
    background: var(--tab);
    color: var(--footer-grey);
    font-family: "Open Sans", Arial, sans-serif;
    font-size: 22px;
    display: flex; align-items: center; justify-content: center;
  }
</style>
</head>
<body>
<main class="page">
  <div class="connector" style="left:155px; height:150px; background:var(--yellow);"></div>
  <div class="connector" style="left:258px; height:382px; background:var(--magenta);"></div>
  <div class="connector" style="left:361px; height:150px; background:var(--green);"></div>
  <div class="connector" style="left:464px; height:382px; background:var(--red);"></div>
  <div class="connector" style="left:566px; height:150px; background:var(--lavender);"></div>
  <div class="connector" style="left:669px; height:382px; background:var(--blue);"></div>
  <div class="connector" style="left:771px; height:150px; background:var(--coral);"></div>

  <header class="title-bar"><h1>Claim Was Denied</h1></header>

  <div class="reason row-top dark-text" style="left:86px; background:var(--yellow);">Auth /<br>Referral<br>Needed</div>
  <div class="reason row-top dark-text" style="left:292px; background:var(--green);">Duplicate</div>
  <div class="reason row-top" style="left:498px; background:var(--lavender);">Global<br>Inclusive</div>
  <div class="reason row-top" style="left:702px; background:var(--coral);">Past<br>Timely<br>Filing</div>

  <div class="reason row-bottom" style="left:190px; background:var(--magenta);">Coding /<br>Billing<br>Issues</div>
  <div class="reason row-bottom" style="left:395px; background:var(--red);">Non-<br>Covered<br>Charge</div>
  <div class="reason row-bottom small-text" style="left:600px; background:var(--blue);">Additional<br>Information<br>Requested</div>

  <div class="footer-url">www.claimguidebook.net</div>
  <div class="page-number">1</div>
</main>
</body>
</html>
```